The Harvest Compass

Clearing Away the Clutter to the Habits That Hold.

Nutrition book

Target Market(s)

People looking to be or get healthy and eat right.

```html
<!DOCTYPE html>
<html lang="en">
<head>
<meta charset="utf-8">
<title>Sure, If — The Harvest Compass</title>
<link rel="stylesheet" href="https://fonts.googleapis.com/css2?family=Montserrat:wght@700;800&family=Rubik:wght@800&display=swap">
<style>
  :root {
    --cover-red: #b80000;
    --ink-white: #ffffff;
    --ink-black: #111111;
    --paper: #ececec;
    --paper-shade: #d8d8d8;
  }
  * { margin: 0; padding: 0; box-sizing: border-box; }
  html, body { width: 728px; height: 1200px; overflow: hidden; background: var(--cover-red); }
  .cover {
    position: relative;
    width: 728px;
    height: 1200px;
    background: var(--cover-red);
    overflow: hidden;
  }
  .series-name {
    position: absolute;
    top: 88px;
    left: 0;
    width: 756px;
    text-align: center;
    font-family: "Montserrat", sans-serif;
    font-weight: 800;
    font-size: 34px;
    letter-spacing: 1.5px;
    color: var(--ink-white);
    text-transform: uppercase;
  }
  .title {
    position: absolute;
    left: 0;
    width: 728px;
    text-align: center;
    font-family: "Rubik", sans-serif;
    font-weight: 800;
    color: var(--ink-white);
    line-height: 1;
  }
  .title-lead {
    top: 292px;
    font-size: 210px;
    letter-spacing: 2px;
  }
  .title-second {
    top: 532px;
    font-size: 220px;
    letter-spacing: 4px;
  }
  .struck {
    position: relative;
    display: inline-block;
  }
  .struck::after {
    content: "";
    position: absolute;
    left: -40px;
    right: -40px;
    top: 54%;
    height: 18px;
    background: var(--ink-black);
    border-radius: 3px;
  }
  .paper-strip {
    position: absolute;
    left: 0;
    top: 0;
    width: 728px;
    height: 1200px;
  }
  .tagline {
    position: absolute;
    top: 990px;
    left: 110px;
    width: 580px;
    text-align: center;
    font-family: "Montserrat", sans-serif;
    font-weight: 700;
    font-size: 34px;
    line-height: 58px;
    color: var(--ink-black);
    text-transform: uppercase;
  }
</style>
</head>
<body>
<main class="cover">
  <p class="series-name">The Harvest Compass</p>

  <h1 class="title title-lead">SURE,</h1>
  <h2 class="title title-second"><span class="struck">IF</span></h2>

  <svg class="paper-strip" viewBox="0 0 977 1610" role="img" aria-label="Torn paper strip holding the tagline">
    <path fill="var(--paper)" d="M0 1222 L60 1212 L130 1218 L200 1200 L280 1206 L360 1192 L420 1198 L500 1186 L580 1196 L650 1190 L720 1202 L800 1196 L870 1208 L930 1214 L977 1210 L977 1575 L900 1570 L820 1580 L740 1568 L660 1576 L580 1566 L500 1574 L420 1566 L340 1572 L260 1564 L180 1570 L120 1562 L118 1610 L0 1610 Z"/>
    <path fill="var(--paper-shade)" d="M0 1222 L60 1212 L130 1218 L200 1200 L280 1206 L360 1192 L420 1198 L500 1186 L580 1196 L650 1190 L720 1202 L800 1196 L870 1208 L930 1214 L977 1210 L977 1246 L860 1238 L700 1232 L500 1226 L300 1232 L120 1240 L0 1250 Z" opacity="0.6"/>
    <path fill="var(--paper-shade)" d="M0 1250 L118 1240 L118 1610 L0 1610 Z" opacity="0.45"/>
  </svg>

  <p class="tagline">Clearing away the clutter<br>to the habits that hold.</p>
</main>
</body>
</html>
```